Handy man Company business card

need branded business card for my new company, this design will transfer to car wrap design what winner will be asked to design

I will need original file so I can edit it in the end.

Also like to have some inspirational quote like "ONE CALL WE DO IT ALL"
"We do it right" can be added to logo side

Like to try to see large 1 800 000 0000 number on front with large logo

Size bigger then standard business card

I like to integrate LAS VEGAS sign to one of sides

Target Market(s)

Handy man services, Home renovation and remodeling

Industry/Entity Type

Handyman

Contact Information for Business Card

Tool Baron LLC.
Name: BORIS LENKOVA
Phone "Temporary": 000 000 0000
Adress: 2715 Fenmore Ct, Las Vegas NV 89147
Website: www.toolbaron.vegas
Email: info@toolbaron.vegas

Requirements
Must have
• Two side
• side n1: LOGO
• side n2: INFO
Nice to have
• Like to have some interesting idea for client to remember!
• With logo added to both side at different stile
Should not have
• Standard design,

```html
<!DOCTYPE html>
<html lang="en">
<head>
<meta charset="utf-8">
<title>Tool Baron — Business Card</title>
<link href="https://fonts.googleapis.com/css2?family=Lato:wght@400;700;900&display=swap" rel="stylesheet">
<style>
  :root {
    --navy: #1b2d3a;
    --amber: #e9a328;
    --ink: #33302a;
    --paper: #f1f1f3;
    --white: #ffffff;
  }
  * { margin: 0; padding: 0; box-sizing: border-box; }
  html, body {
    width: 1200px; height: 1200px; overflow: hidden;
    background: var(--paper);
    font-family: "Lato", sans-serif;
  }
  .card {
    position: absolute;
    left: 354px; width: 528px; height: 302px;
    overflow: hidden;
  }
  .card--info { top: 234px; background: var(--amber); }
  .card--logo { top: 638px; background: var(--navy); }

  .info-header {
    position: absolute; left: 0; top: 0; width: 100%; height: 142px;
    background: var(--navy);
  }
  .brand {
    position: absolute; display: flex; align-items: center;
  }
  .brand__mascot {
    border-radius: 10px;
    background: linear-gradient(180deg, #e9a328 0%, #f0c08a 35%, #7fb8dc 55%, #e9a328 100%);
  }
  .brand__name {
    color: var(--white); font-weight: 900; white-space: nowrap; letter-spacing: 0.5px;
  }
  .info-header .brand { left: 126px; top: 26px; height: 92px; gap: 14px; }
  .info-header .brand__mascot { width: 48px; height: 92px; }
  .info-header .brand__name { font-size: 44px; }

  .card--logo .brand { left: 78px; top: 90px; height: 124px; gap: 18px; }
  .card--logo .brand__mascot { width: 60px; height: 124px; }
  .card--logo .brand__name { font-size: 60px; }

  .name-bar {
    position: absolute; left: 60px; top: 164px; width: 468px; height: 46px;
    background: var(--navy);
    clip-path: polygon(0 0, 100% 0, 100% 100%, 42px 100%);
    display: flex; align-items: center; justify-content: center;
    padding-left: 40px;
  }
  .name-bar__text {
    color: var(--white); font-size: 23px; font-weight: 700; letter-spacing: 0.3px;
  }

  .contact {
    position: absolute; display: flex; flex-direction: column; gap: 8px;
    color: var(--ink); font-size: 12.5px; letter-spacing: 0.4px;
  }
  .contact--left { left: 35px; top: 236px; }
  .contact--right { left: 318px; top: 236px; }
  .contact__row { display: flex; align-items: center; gap: 11px; height: 13px; }
  .contact__icon { width: 14px; height: 14px; flex: none; }
</style>
</head>
<body>

<section class="card card--info" aria-label="Business card, information side">
  <div class="info-header">
    <div class="brand">
      <div class="brand__mascot" role="img" aria-label="Cartoon handyman mascot in cap and overalls"></div>
      <span class="brand__name">Tool Baron</span>
    </div>
  </div>

  <div class="name-bar"><span class="name-bar__text">BORIS LENKOVA</span></div>

  <div class="contact contact--left">
    <div class="contact__row">
      <svg class="contact__icon" viewBox="0 0 14 14" aria-hidden="true">
        <rect x="0.6" y="0.6" width="12.8" height="12.8" fill="none" stroke="var(--ink)" stroke-width="1.2"/>
        <path d="M7 11 C5 8 4.3 7 4.3 5.6 A2.7 2.7 0 0 1 9.7 5.6 C9.7 7 9 8 7 11Z" fill="var(--ink)"/>
        <circle cx="7" cy="5.6" r="1" fill="var(--amber)"/>
      </svg>
      <span>000 000 0000</span>
    </div>
    <div class="contact__row">
      <svg class="contact__icon" viewBox="0 0 14 14" aria-hidden="true">
        <rect x="0.6" y="0.6" width="12.8" height="12.8" fill="none" stroke="var(--ink)" stroke-width="1.2"/>
        <path d="M4 3.5 L5.6 3.2 L6.4 5.4 L5.4 6.2 C5.9 7.4 6.7 8.2 7.8 8.7 L8.6 7.7 L10.7 8.5 L10.4 10.1 C7 10.3 3.8 7.2 4 3.5Z" fill="var(--ink)"/>
      </svg>
      <span>2715 Fenmore Ct, Las Vegas NV 89147</span>
    </div>
  </div>

  <div class="contact contact--right">
    <div class="contact__row">
      <svg class="contact__icon" viewBox="0 0 14 14" aria-hidden="true">
        <rect x="0.6" y="0.6" width="12.8" height="12.8" fill="none" stroke="var(--ink)" stroke-width="1.2"/>
        <circle cx="7" cy="7" r="3.8" fill="none" stroke="var(--ink)" stroke-width="1"/>
        <ellipse cx="7" cy="7" rx="1.6" ry="3.8" fill="none" stroke="var(--ink)" stroke-width="0.8"/>
        <line x1="3.2" y1="7" x2="10.8" y2="7" stroke="var(--ink)" stroke-width="0.8"/>
      </svg>
      <span>www.toolbaron.vegas</span>
    </div>
    <div class="contact__row">
      <svg class="contact__icon" viewBox="0 0 14 14" aria-hidden="true">
        <rect x="0.6" y="0.6" width="12.8" height="12.8" fill="none" stroke="var(--ink)" stroke-width="1.2"/>
        <rect x="3.2" y="4.3" width="7.6" height="5.4" fill="var(--ink)"/>
        <path d="M3.4 4.5 L7 7.4 L10.6 4.5" fill="none" stroke="var(--amber)" stroke-width="0.8"/>
      </svg>
      <span>info@toolbaron.vegas</span>
    </div>
  </div>
</section>

<section class="card card--logo" aria-label="Business card, logo side">
  <div class="brand">
    <div class="brand__mascot" role="img" aria-label="Cartoon handyman mascot in cap and overalls"></div>
    <span class="brand__name">Tool Baron</span>
  </div>
</section>

</body>
</html>
```